Eyewear store

-The design must be based around the attached HPID (home page information design) called Lens at Marlowe HPID. I've attached Word and PDF versions - these are the same. The table boxes are just for approximate placement of information – you DON'T have to box everything in and you can arrange these. All fonts used in the HPID are only examples - you can use any Google font you wish.
- Information only is in orange text. Copy to go on the design in black text. Some instructions are in the HPID. Please be creative!
-The design needs to be modern. Colours are to be brown, green, black and white ...refer to the shop images in the HPID. Keep it clean and simple, don't need to use all the colours.
- I've provided the images for the site but these are just to show style, use any similar images, but they must be free images.
Width of content will be 1100 pixels when implemented as a web page. Header height (without nav bar) 150-160 pixels.
If your design is chosen the winning PSD file will have to be provided as follows…
1. Canvas size of 2000px x 2000px - 72ppi in Adobe Photoshop (CS5 compatible)
2. Width of content section is 1100px wide - centered in the canvas
3. Any button rollovers/hovers in the PSD as hidden layers.
4. All fonts used must be Google fonts (except for the fonts in the header at the top of the page).
5. You will need to supply the chosen home page plus one example page (example page as a style guide for how all other pages will look). Example page is only the header and navigational bar at the top, an empty sector in the middle with a column (180 px wide) which can be left or right aligned which means the main sector is 920 pixels wide, and then the footer at the bottom of the page
Checklist - http://pagecraftlist.example/
Target Market(s)
Fashion Eyewear lovers
Mid age women
Sportspeople
Teenagers who need prescription
Non-glasses wearers - People looking to buy branded sunglasses (fashion conscious people of all ages)
Industry/Entity Type
Store
Look and feel
Each slider illustrates characteristics of the customer's brand and the style your logo design should communicate.

```html
<!DOCTYPE html>
<html lang="en">
<head>
<meta charset="utf-8">
<title>Lens at Marlowe – Creative Eyewear</title>
<link href="https://fonts.googleapis.com/css2?family=Lato:ital,wght@0,400;0,700;1,700&family=Ubuntu:wght@400;500&display=swap" rel="stylesheet">
<style>
:root{
  --brown:#674220;
  --brown-dark:#553516;
  --brown-light:#8a5e35;
  --blue:#1e6f93;
  --blue-dark:#175a78;
  --ink:#333;
  --muted:#666;
  --panel:#ececec;
  --footer:#f3f3f3;
  --white:#fff;
}
*{margin:0;padding:0;box-sizing:border-box}
html,body{width:898px;height:1200px;overflow:hidden;background:var(--white)}
body{position:relative;font-family:'Lato',sans-serif;color:var(--ink)}
.abs{position:absolute}

/* header */
.brand{left:63px;top:36px;font-weight:700;font-size:25px;color:var(--blue-dark);letter-spacing:.5px}
.brand small{display:block;font-size:11px;font-weight:400;color:var(--blue);text-align:right;letter-spacing:1px;margin-top:2px}
.tagline{left:345px;top:36px;width:280px;font-style:italic;font-weight:700;font-size:14px;line-height:25px;color:var(--brown-light)}
.tagline span{display:block;padding-left:42px}
.social{left:678px;top:15px;display:flex;gap:7px}
.social i{width:21px;height:21px;border-radius:50%;background:#f2f2f2;border:1px solid #d6d6d6}
.contact{left:680px;font-size:11px;color:var(--ink);display:flex;align-items:center;gap:8px}

/* nav */
.nav{left:0;top:106px;width:898px;height:42px;background:var(--brown);display:flex;padding-left:63px}
.nav a{color:var(--white);font-size:11.5px;text-decoration:none;padding:0 12px;line-height:42px;border-right:1px solid rgba(255,255,255,.12)}
.nav a.active{background:var(--brown-light);font-weight:700}

/* hero */
.hero{left:0;top:148px;width:898px;height:335px;overflow:hidden;
  background:
    radial-gradient(ellipse 120px 150px at 250px 170px,rgba(214,178,150,.9),rgba(214,178,150,0) 100%),
    radial-gradient(ellipse 260px 260px at 270px 150px,rgba(88,60,40,.85),rgba(88,60,40,0) 100%),
    radial-gradient(ellipse at 40% 40%,#f1f1f1 0%,#c9c9c9 55%,#9a9a9a 100%)}
.hero-photo{position:absolute;inset:0}
.caption-box{position:absolute;left:63px;top:238px;width:432px;height:74px;background:rgba(60,60,60,.82)}
.caption{position:absolute;left:69px;top:242px;width:430px;color:var(--white);font-family:Arial,sans-serif;font-weight:700;font-size:24px;line-height:33px}
.tile{left:670px;width:164px;height:58px;background:linear-gradient(90deg,#f7f7f7,#d5d5d5);border:1px solid #fff;color:#444;font-size:15px;padding:4px 6px;line-height:18px}
.tile.dark{background:linear-gradient(90deg,#7b3a22,#3a2a22);color:#f1e3d5}
.tile.pink{background:linear-gradient(90deg,#e46f8f,#d8d8d8);text-align:right}
.tile.eye{background:linear-gradient(90deg,#7fa8c4,#e8e8e8);text-align:right}
.side-arrow{top:282px;width:22px;height:44px;background:#e6e6e6}

/* cards */
.card{top:514px;width:246px;height:294px;background:var(--panel);border-radius:3px}
.card h2{height:40px;background:linear-gradient(#2a84ab,var(--blue-dark));color:var(--white);font-family:'Ubuntu',sans-serif;font-weight:500;font-size:12.5px;text-align:center;line-height:15px;padding-top:5px;border-radius:3px 3px 0 0}
.card .photo{height:117px;margin-top:2px}
.card p{font-size:9px;line-height:14px;color:#444;padding:14px 14px 0 14px}
.card p+p{padding-top:6px}
.more{position:absolute;left:50%;bottom:0;transform:translateX(-50%);width:98px;height:20px;background:var(--brown);clip-path:polygon(12% 0,88% 0,100% 100%,0 100%);color:var(--white);font-size:10px;font-weight:700;text-align:center;line-height:21px}

/* brands */
.brands-title{left:0;top:840px;width:898px;text-align:center;font-family:'Ubuntu',sans-serif;font-weight:400;font-size:21px;color:var(--brown-dark)}
.brands{left:100px;top:898px;width:698px;display:flex;justify-content:space-between;align-items:center}
.brands span{font-family:'Ubuntu',sans-serif;font-size:13px;font-weight:500;color:#444}

/* footer */
.footer{left:0;top:975px;width:898px;height:196px;background:var(--footer)}
.foot-h{font-size:13px;font-weight:400;color:var(--brown-dark)}
.foot-rule{height:1px;background:#ddd;margin-top:6px}
.links{font-size:9px;line-height:18.5px;color:#444;list-style:none;margin-top:4px}
.links li::before{content:"›";margin-right:8px;color:#777}
.hours{font-size:10.5px;line-height:16px;color:#333}
.store{height:26px;background:var(--white);border:1px solid #ddd;font-size:12px;font-weight:700;padding-left:4px;line-height:26px}
.store.navy{background:#17337a;color:var(--white);border:none}
.view{font-size:9px;font-style:italic;color:#666;text-decoration:underline}
.bottom{left:0;top:1171px;width:898px;height:29px;background:var(--brown);color:var(--white);font-size:9.5px;line-height:29px;padding-left:65px}
.cards-pay{right:63px;top:1178px;display:flex;gap:4px}
.cards-pay i{width:26px;height:15px;border-radius:2px;background:#2c4ea3}
.cards-pay i:first-child{background:#e8e8e8}
</style>
</head>
<body>

<header>
  <div class="abs brand">LENS AT MARLOWE<small>creative eyewear</small></div>
  <p class="abs tagline">For stylish sunglasses, prescription <span>glasses and eye exams in Harbourton</span></p>
  <div class="abs social" aria-label="Social links"><i></i><i></i><i></i><i></i></div>
  <div class="abs contact" style="top:50px">
    <svg width="10" height="11" viewBox="0 0 10 11"><path d="M2 0l2 2.5-1 1.3c.7 1.6 1.9 2.9 3.4 3.6l1.2-1L10 8.5 8.6 10.4C4.3 10 .3 5.6 0 1.5z" fill="#674220"/></svg>
    (07) 555 0142</div>
  <div class="abs contact" style="top:72px">
    <svg width="10" height="12" viewBox="0 0 10 12"><path d="M5 0a4.5 4.5 0 0 0-4.5 4.5C.5 8 5 12 5 12s4.5-4 4.5-7.5A4.5 4.5 0 0 0 5 0zm0 6.2a1.7 1.7 0 1 1 0-3.4 1.7 1.7 0 0 1 0 3.4z" fill="#674220"/></svg>
    14B Marlowe Street, Harbourton</div>
</header>

<nav class="abs nav">
  <a class="active">Home</a><a>About</a><a>Eyewear</a><a>Book an Eye Exam</a><a>Specials/Promotions</a><a>All About Eyes</a><a>News</a><a>Articles</a><a>Other Stores</a><a>Contact</a>
</nav>

<section>
  <div class="abs hero">
    <div class="hero-photo" role="img" aria-label="Woman with brown curly hair wearing large white sunglasses against a soft grey background"></div>
    <div class="caption-box"></div>
    <p class="caption">Three stores, one vision &amp;<br>All you need is the right pair of<br>specs</p>
  </div>
  <div class="abs side-arrow" style="left:0;border-radius:0 22px 22px 0"><svg width="22" height="44"><path d="M13 15l-6 7 6 7" fill="#999"/></svg></div>
  <div class="abs side-arrow" style="right:0;border-radius:22px 0 0 22px"><svg width="22" height="44"><path d="M9 15l6 7-6 7" fill="#999"/></svg></div>
  <div class="abs tile" style="top:155px" role="img" aria-label="Eyewear tile with aviator sunglasses">Eyewear</div>
  <div class="abs tile eye" style="top:221px;text-align:left" role="img" aria-label="Book an eye exam tile with close-up eye">Book an<br>Eye Exam</div>
  <div class="abs tile dark" style="top:287px" role="img" aria-label="Specials tile with sunglasses">Specials &amp;<br>Promotios</div>
  <div class="abs tile pink" style="top:352px" role="img" aria-label="What's new tile with woman in sunglasses">What's New<br>in Store</div>
  <div class="abs tile eye" style="top:418px" role="img" aria-label="All about eyes tile with close-up eye">All About<br>Eyes</div>
</section>

<section>
  <article class="abs card" style="left:64px">
    <h2>Largest sunglasses selection<br>in Harbourton</h2>
    <div class="photo" role="img" aria-label="Young woman in heart-shaped sunglasses" style="background:linear-gradient(90deg,#d9c3a6,#eef0e6)"></div>
    <p>For the latest brands and designer sunglasses come in and see the friendly team at Lens at Marlowe. There's something for everyone with thousands of glasses in store – view our selection online now.</p>
    <p>We're also the exclusive stockist in Harbourton of Solano sunglasses and optical frames.</p>
    <span class="more">MORE INFO</span>
  </article>
  <article class="abs card" style="left:328px">
    <h2>Harbourton's Prescription glasses<br>experts – perfect fit guaranteed</h2>
    <div class="photo" role="img" aria-label="Woman wearing aviator sunglasses" style="background:linear-gradient(90deg,#6b4a36,#c79d7e)"></div>
    <p>Lens at Marlowe is your One-Stop-Shop Eyecare store and have a huge range of prescription lenses, contact lenses and the very latest European trend-setting fashion eye-wear.</p>
    <p style="padding-top:12px">Take a look at our selection of prescription glasses now.</p>
    <span class="more">MORE INFO</span>
  </article>
  <article class="abs card" style="left:590px">
    <h2>For eye exams in the heart<br>of Harbourton</h2>
    <div class="photo" role="img" aria-label="Close-up eye with an eye chart overlay" style="background:linear-gradient(90deg,#5c7f98,#c8d5de)"></div>
    <p>Lens at Marlowe offers complete eye examinations in store. Our Optometrists offer free annual check-ups and glasses fitting.</p>
    <p>And all our glasses come with a full replacement warranty on all new frames and lenses sold – Book an appointment now.</p>
    <span class="more">MORE INFO</span>
  </article>
</section>

<section>
  <h2 class="abs brands-title">Brands Include</h2>
  <svg class="abs" style="left:66px;top:899px" width="14" height="28"><path d="M12 2L2 14l10 12" stroke="#1e6f93" stroke-width="4" fill="none"/></svg>
  <svg class="abs" style="left:810px;top:899px" width="14" height="28"><path d="M2 2l10 12-10 12" stroke="#1e6f93" stroke-width="4" fill="none"/></svg>
  <div class="abs brands">
    <span>Verlaine</span><span>Kaimoana</span><span>Ridgeline</span><span>Castellan</span><span>Solano</span><span>Orsetti</span><span>Castellan</span>
  </div>
</section>

<footer>
  <div class="abs footer"></div>
  <div class="abs" style="left:63px;top:990px;width:231px">
    <h3 class="foot-h">Quick Links</h3><div class="foot-rule"></div>
    <div style="display:flex;gap:60px">
      <ul class="links"><li>Home</li><li>About</li><li>Eyewear</li><li>Book an Eye Exam</li><li>Specials/Promotions</li><li>All About Eyes</li><li>News</li></ul>
      <ul class="links"><li>Articles</li><li>Other Stores</li><li>Contact</li></ul>
    </div>
  </div>
  <div class="abs" style="left:363px;top:990px;width:183px">
    <h3 class="foot-h"><svg width="12" height="12" style="vertical-align:-1px;margin-right:6px"><circle cx="6" cy="6" r="5" stroke="#674220" stroke-width="1.5" fill="none"/><path d="M6 3v3h2.5" stroke="#674220" stroke-width="1.3" fill="none"/></svg>Open hours</h3>
    <div class="foot-rule"></div>
    <div class="hours" style="padding:4px 0 0 23px">Monday: <b>Friday: 9:00am - 5:00pm</b><br>Saturday: <b>9:00am - 01:00pm</b><br>Statutory Holidays: <b>Closed</b></div>
    <h3 class="foot-h" style="margin-top:20px"><svg width="10" height="12" style="vertical-align:-1px;margin-right:8px"><path d="M5 0a4.5 4.5 0 0 0-4.5 4.5C.5 8 5 12 5 12s4.5-4 4.5-7.5A4.5 4.5 0 0 0 5 0zm0 6.2a1.7 1.7 0 1 1 0-3.4 1.7 1.7 0 0 1 0 3.4z" fill="#674220"/></svg>Address</h3>
    <div class="foot-rule"></div>
    <div class="hours" style="font-size:9.5px;line-height:14px;padding:4px 0 0 23px;color:#555">14B Marlowe Street<br>Harbourton 4500<br>New Zealand</div>
  </div>
  <div class="abs" style="left:629px;top:990px;width:175px">
    <h3 class="foot-h">Other stores</h3>
    <div class="store navy" style="margin-top:12px;width:175px">Riverside Eyecare Centre</div>
    <div class="view" style="margin:5px 0 0 4px">View website</div>
    <div class="store" style="margin-top:18px;width:175px">Kestrel Eyecare</div>
    <div class="view" style="margin:5px 0 0 0">View website</div>
  </div>
  <div class="abs bottom">Copyright © 2015 Lens at Marlowe. All Rights Reserved</div>
  <div class="abs cards-pay" aria-label="Accepted payment methods"><i></i><i></i><i></i><i></i><i></i></div>
</footer>

</body>
</html>
```